Letterhead for clinic notes, test reports, and business cards

I need business card and letterheads for a medical clinic with the following:
1- Business cards. The back should allow for space for date and time of next appointments (few lines would do)
2- Letterhead for clinic notes
3- Letterhead for test reports.

Feel free to use whats included for examples. I value creativity so be creative.

Target Market(s)

Patients, referring physicians.

Industry/Entity Type

Health Care

Requirements
Must have
• Must use current logo.
• Must look good on white background
• Letterhead and reports must look good faxed.
• Please use themes of the current logo. Another possible color to use is grey as well (www.brackenvale-cardio.org - use the font color in the text of that website)

```html
<!DOCTYPE html>
<html lang="en">
<head>
<meta charset="utf-8">
<title>Brackenvale Cardio Institute – Stationery</title>
<link href="https://fonts.googleapis.com/css2?family=Tinos:wght@400&display=swap" rel="stylesheet">
<style>
  :root{
    --backdrop:#6d7890;
    --navy:#24427f;
    --red:#d0322f;
    --blush:#f6d6d4;
    --ice:#d8ecf6;
    --rule:#9aa6bd;
    --paper:#ffffff;
  }
  *{box-sizing:border-box;margin:0;padding:0}
  html,body{width:1200px;height:1200px;overflow:hidden}
  body{background:var(--backdrop);position:relative;font-family:"Tinos",serif;color:var(--navy)}

  .sheet{
    position:absolute;background:var(--paper);
    background-image:
      radial-gradient(ellipse at 55% 55%, rgba(255,255,255,1) 35%, rgba(255,255,255,0) 75%),
      linear-gradient(135deg,var(--blush) 0%,#fff 50%,var(--ice) 100%);
    box-shadow:0 6px 18px rgba(30,40,60,.35);
  }

  .letterhead{left:560px;top:170px;width:560px;height:792px}
  .letterhead .brand{position:absolute;left:40px;top:42px}
  .brand-name{display:flex;align-items:center;gap:10px;font-size:22px;letter-spacing:1.5px;text-transform:uppercase;color:var(--navy);line-height:1}
  .brand-dot{width:18px;height:18px;border-radius:50%;background:var(--red);flex:none}
  .letterhead .contact{position:absolute;right:40px;top:46px;font-size:11.5px;line-height:1.55;display:grid;grid-template-columns:auto auto auto;column-gap:18px;text-align:left}
  .lbl{color:var(--red)}

  .card{width:420px;height:240px}
  .card-back{left:60px;top:330px}
  .card-front{left:60px;top:640px}

  .appointments{position:absolute;left:28px;top:24px;right:28px}
  .appointments h2{font-weight:400;font-size:20px;margin-bottom:16px}
  .appt-row{display:flex;gap:16px;font-size:13px;margin-bottom:18px}
  .appt-field{display:flex;align-items:flex-end;gap:6px}
  .appt-field.date{flex:1.3}
  .appt-field.time{flex:1}
  .appt-line{flex:1;border-bottom:1px dotted var(--rule);height:12px}

  .card-front .brand{position:absolute;left:26px;top:34px}
  .card-front .brand-name{font-size:15px;letter-spacing:1px}
  .card-front .brand-dot{width:13px;height:13px}
  .card-divider{position:absolute;left:205px;top:30px;bottom:30px;width:1px;background:var(--rule)}
  .card-front .contact{position:absolute;left:222px;top:92px;font-size:11px;line-height:1.6}
</style>
</head>
<body>

<section class="sheet letterhead" aria-label="Letterhead">
  <div class="brand">
    <div class="brand-name"><span class="brand-dot"></span>Brackenvale Cardio Institute</div>
  </div>
  <div class="contact" style="top:86px">
    <div><span class="lbl">T.</span> 555.010.4821<br><span class="lbl">F.</span> 555.010.4830</div>
    <div>www.brackenvale-cardio.org<br>contact@brackenvale-cardio.org</div>
    <div>1180 Mercer Lane<br>Suite 305, Halden ON K2P4R1</div>
  </div>
</section>

<section class="sheet card card-back" aria-label="Business card back – appointments">
  <div class="appointments">
    <h2>Appointments</h2>
    <div class="appt-row"><div class="appt-field date">Date<span class="appt-line"></span></div><div class="appt-field time">Time<span class="appt-line"></span></div></div>
    <div class="appt-row"><div class="appt-field date">Date<span class="appt-line"></span></div><div class="appt-field time">Time<span class="appt-line"></span></div></div>
    <div class="appt-row"><div class="appt-field date">Date<span class="appt-line"></span></div><div class="appt-field time">Time<span class="appt-line"></span></div></div>
    <div class="appt-row"><div class="appt-field date">Date<span class="appt-line"></span></div><div class="appt-field time">Time<span class="appt-line"></span></div></div>
  </div>
</section>

<section class="sheet card card-front" aria-label="Business card front">
  <div class="brand">
    <div class="brand-name"><span class="brand-dot"></span>Brackenvale<br>Cardio Institute</div>
  </div>
  <div class="card-divider"></div>
  <div class="contact">
    <span class="lbl">T.</span> 555.010.4821<br>
    <span class="lbl">F.</span> 555.010.4830<br>
    www.brackenvale-cardio.org<br>
    contact@brackenvale-cardio.org<br>
    1180 Mercer Lane<br>
    Suite 305, Halden ON K2P4R1
  </div>
</section>

</body>
</html>
```